The Tarnvale Classic for Midfield Legends™

Please go to www.tarnvaleclassic.example and if you are a professional web designer you know what needs to be done!
I need a fresh, modern but still 'credible' design (authority!) - after all the event is an official World Championship!
Content (text, pics etc.) remains the same.
A new, trademarked logo has been developed and needs to be used throughout the site.
The site must include the possibility to be able to update/change content by ourselfs using a simple CMS.
Project duration: 5 days or less.
Main reason being for such a short period of time: we are AT PRESENT in negociations with all kinds of stakeholders and would like to impress them ASAP!
Could be an ongoing job for next couple of months.
Key words: official World Championship, golf, football, first sports cross over event ever, authority, fun, BRAZIL (hosting country), excitement, television, country's honour, another Ardent Shield, PASSION!!
Pictures on website can be used - our/my responsibility.
Good luck!

Target Market(s)

(ex) Footballers - european soccer.
Golfers
People interested in sports

Industry/Entity Type

Event

Requirements
Must have
• Golf
Football
Brazil
Authority
World Championship

```html
<!DOCTYPE html>
<html lang="en">
<head>
<meta charset="utf-8">
<title>The Tarnvale Classic for Midfield Legends™</title>
<link rel="stylesheet" href="https://fonts.googleapis.com/css2?family=Oswald:wght@500;600&family=Ubuntu:wght@400;500&family=Roboto:wght@400;500;700&family=Parisienne&display=swap">
<style>
:root{
  --gold:#c9a94a;
  --gold-dark:#8a7430;
  --gold-text:#c8a64b;
  --grass-light:#5f9a2e;
  --grass-mid:#3e7a1d;
  --grass-dark:#1f4a0e;
  --bar-top:#3a3a3a;
  --bar-bottom:#1c1c1c;
  --field:#8d8d8d;
  --field-text:#e6e6e6;
  --page:#141414;
  --page-light:#262626;
  --text:#e8e8e8;
  --muted:#a0a0a0;
  --rule:#3a3a3a;
  --white:#ffffff;
}
*{box-sizing:border-box;margin:0;padding:0}
html,body{width:1168px;height:1200px;overflow:hidden;background:var(--page)}
body{font-family:"Roboto",sans-serif;color:var(--text);position:relative}

.hero{position:absolute;left:0;top:0;width:1168px;height:475px;border-top:4px solid var(--gold)}
.hero-photo{position:absolute;inset:0;background:
  radial-gradient(circle at 570px 310px,#f2f2f0 0 80px,transparent 82px),
  radial-gradient(ellipse at 50% 40%,var(--grass-light),var(--grass-mid) 55%,var(--grass-dark))}
.logo{position:absolute;left:110px;top:0;width:201px;height:141px;background:linear-gradient(#fdfdfd,#dcdcdc);border:3px solid #eee;border-top:0;box-shadow:0 2px 8px rgba(0,0,0,.4);display:flex;flex-direction:column;align-items:center;justify-content:center;gap:10px}
.logo-mark{width:46px;height:46px;border-radius:50%;background:var(--gold)}
.logo-name{font-family:"Ubuntu",sans-serif;font-size:10px;font-weight:500;color:var(--gold-dark);text-align:center;line-height:1.3;text-transform:uppercase;letter-spacing:.5px;padding:0 8px}
.phone{position:absolute;right:106px;top:24px;display:flex;align-items:center;gap:6px;font-family:"Ubuntu",sans-serif;font-size:17px;color:var(--white);text-shadow:0 1px 2px rgba(0,0,0,.5)}
.nav{position:absolute;right:106px;top:86px;display:flex;gap:19px;font-family:"Oswald",sans-serif;font-size:19px;font-weight:600;text-transform:uppercase;text-shadow:0 1px 3px rgba(0,0,0,.6)}
.nav a{color:#f4c232;text-decoration:none}
.nav a.current{color:var(--white)}
.quote{position:absolute;top:205px;font-family:"Parisienne",cursive;font-size:31px;line-height:44px;color:var(--white);text-shadow:0 2px 4px rgba(0,0,0,.6);word-spacing:6px}
.quote-left{left:112px;width:330px}
.quote-right{left:655px;width:420px}
.dots{position:absolute;right:107px;top:456px;display:flex;gap:10px}
.dots span{width:10px;height:10px;background:#e8e8e8;box-shadow:0 0 2px rgba(0,0,0,.5)}
.dots span.active{background:#9a8a6a}

.quick{position:absolute;left:0;top:475px;width:1168px;height:77px;background:linear-gradient(var(--bar-top),var(--bar-bottom));border-top:1px solid #555;border-bottom:1px solid #000}
.quick-title{position:absolute;left:104px;top:7px;font-family:"Oswald",sans-serif;font-size:25px;line-height:31px;font-weight:500;color:var(--field-text);text-transform:uppercase}
.field{position:absolute;top:24px;height:34px;background:var(--field);border:1px solid #a5a5a5;border-radius:2px;font-size:14px;color:var(--field-text);padding:8px 10px}
.submit{position:absolute;left:956px;top:22px;width:99px;height:37px;background:linear-gradient(#b8a052,#8c7430);border:1px solid #c9b36a;color:var(--white);font-family:"Ubuntu",sans-serif;font-size:19px;font-weight:500;display:flex;align-items:center;justify-content:center}

.main{position:absolute;left:0;top:552px;width:1168px;height:648px;background:radial-gradient(ellipse at 45% 30%,var(--page-light),var(--page) 70%)}
.section-title{font-family:"Ubuntu",sans-serif;font-size:22px;font-weight:500;color:var(--gold-text);display:flex;align-items:center;gap:8px}
.intro{position:absolute;left:112px;top:24px;width:600px}
.intro .section-title{margin-bottom:20px}
.emblem{width:22px;height:22px;border-radius:50%;background:var(--gold);margin-right:4px}
.intro-date{font-size:13px;font-weight:500;color:var(--white);margin-bottom:11px}
.intro p{font-size:12.6px;line-height:19.2px;color:var(--text);margin:0 0 16px 2px;text-align:justify}
.news{position:absolute;left:772px;top:24px;width:290px}
.news .section-title{border-bottom:1px solid var(--rule);padding-bottom:6px;margin-bottom:12px}
.news-date{display:flex;align-items:center;gap:8px;font-size:13px;font-weight:500;color:var(--white)}
.news-head{font-size:13px;font-weight:700;color:var(--white);margin:3px 0 2px}
.news p{font-size:12.6px;line-height:19.2px;color:var(--text)}
.more{display:inline-block;margin-top:10px;font-size:13px;font-weight:500;color:var(--gold-text);text-decoration:none}
.rule{position:absolute;left:112px;width:950px;height:1px;background:linear-gradient(90deg,transparent,var(--rule) 15%,var(--rule) 85%,transparent)}
.candidates{position:absolute;left:113px;top:276px}
.candidates .section-title{padding-bottom:8px;border-bottom:1px solid var(--rule);width:220px}
.arrow{position:absolute;top:370px;width:36px;height:36px;border-radius:50%;background:linear-gradient(#8a8a8a,#4a4a4a);border:2px solid #2a2a2a;display:flex;align-items:center;justify-content:center}
.player{position:absolute;top:320px;width:140px;text-align:center}
.portrait{width:130px;height:130px;margin:0 auto;border-radius:50%;border:5px solid #5a5a5a;box-shadow:0 0 0 2px #2a2a2a,0 4px 10px rgba(0,0,0,.6);background:radial-gradient(circle at 50% 40%,#8a7a6a,#3f5f3a 70%)}
.player-name{margin-top:13px;font-size:13px;font-weight:700;color:var(--white)}
.player-country{font-size:13px;font-weight:500;color:var(--gold-text);margin-top:3px}

.footer-nav{position:absolute;left:114px;top:1110px;display:flex;gap:25px;font-family:"Oswald",sans-serif;font-size:19px;font-weight:500;color:#8a8a8a;text-transform:uppercase}
.copy{position:absolute;left:115px;top:1164px;font-size:13px;color:var(--muted)}
.newsletter{position:absolute;left:566px;top:1110px}
.newsletter h3{font-family:"Oswald",sans-serif;font-size:19px;font-weight:500;color:#8a8a8a;text-transform:uppercase;margin-bottom:20px}
.signup{display:flex}
.signup span{width:191px;height:26px;background:#f5f5f5;border:1px solid #ccc;font-size:13.5px;color:#666;padding:4px 8px}
.signup b{width:31px;height:26px;background:#8c7430;border:1px solid #c9b36a;color:var(--white);font-size:11px;display:flex;align-items:center;justify-content:center}
.footer-mark{position:absolute;left:887px;top:1105px;font-family:"Ubuntu",sans-serif;font-size:12px;font-weight:500;color:var(--gold-text);display:flex;align-items:center;gap:8px}
.footer-mark i{width:20px;height:20px;border-radius:50%;background:var(--gold)}
.social{position:absolute;left:888px;top:1159px;display:flex;gap:12px}
.social span{width:27px;height:27px;border-radius:50%;background:#555}
</style>
</head>
<body>

<header class="hero">
  <div class="hero-photo" role="img" aria-label="Close-up photograph of a white golf ball on a tee against a green fairway"></div>
  <div class="logo">
    <span class="logo-mark"></span>
    <span class="logo-name">The Tarnvale Classic<br>for Midfield Legends™</span>
  </div>
  <div class="phone">
    <svg width="22" height="22" viewBox="0 0 24 24" aria-hidden="true"><path fill="#fff" d="M6.6 10.8a15 15 0 0 0 6.6 6.6l2.2-2.2a1 1 0 0 1 1-.25 11.4 11.4 0 0 0 3.6.57 1 1 0 0 1 1 1V20a1 1 0 0 1-1 1A17 17 0 0 1 3 4a1 1 0 0 1 1-1h3.5a1 1 0 0 1 1 1c0 1.25.2 2.45.57 3.57a1 1 0 0 1-.25 1z"/></svg>
    + 34 600 481 926
  </div>
  <nav class="nav">
    <a class="current" href="#">Home</a>
    <a href="#">Event</a>
    <a href="#">Ambassadors</a>
    <a href="#">TVC/Contact</a>
  </nav>
  <p class="quote quote-left">‘Championship is not about money but about countries honour.....!!’</p>
  <p class="quote quote-right">‘Event appeals to a huge audience: 80 million golfers &amp; 300 million footballers world wide.’</p>
  <div class="dots"><span class="active"></span><span></span><span></span><span></span></div>
</header>

<section class="quick">
  <h2 class="quick-title">Quick<br>Contact</h2>
  <div class="field" style="left:220px;width:151px">Name</div>
  <div class="field" style="left:379px;width:191px">Email</div>
  <div class="field" style="left:577px;width:136px">Subject</div>
  <div class="field" style="left:726px;width:217px">Message</div>
  <div class="submit">SUBMIT</div>
</section>

<main class="main">
  <article class="intro">
    <h2 class="section-title"><span class="emblem"></span>The Tarnvale Classic for Midfield Legends ©</h2>
    <p class="intro-date">June 5-8, 2014, Rio de Janeiro, Brazil</p>
    <p>One doesn’t need to be a fanatical supporter of either golf or football to get a sense of just how much interest and excitement the Tarnvale Classic for Midfield Legends© will generate: an A-list of current and former players and coaches from the world’s most popular spectator sport, playing the world’s fastest growing participation sport, on the world’s most beautiful golf courses, just has to be a winner!</p>
    <p>"These guys have performed in front of millions of people on a weekly basis. It will be fascinating to see how they hold their nerves outside their comfort zones but still in a very competitive environment…"</p>
  </article>

  <aside class="news">
    <h2 class="section-title">
      <svg width="17" height="17" viewBox="0 0 16 16" aria-hidden="true"><rect width="16" height="16" rx="2" fill="#8a8a8a"/><circle cx="4.5" cy="11.5" r="1.5" fill="#222"/><path d="M3 7a6 6 0 0 1 6 6M3 3.5A9.5 9.5 0 0 1 12.5 13" stroke="#222" stroke-width="1.6" fill="none"/></svg>
      Latest News
    </h2>
    <div class="news-date">
      <svg width="16" height="15" viewBox="0 0 16 15" aria-hidden="true"><rect x="0.5" y="2" width="15" height="12.5" fill="none" stroke="#8a8a8a"/><rect x="0.5" y="2" width="15" height="3" fill="#8a8a8a"/><path d="M3 7h2v2H3zM7 7h2v2H7zM11 7h2v2h-2zM3 11h2v2H3zM7 11h2v2H7z" fill="#8a8a8a"/></svg>
      October 25 , 2013
    </div>
    <p class="news-head">President BFN: 'Event vitally important'</p>
    <p>A delegation of TVC Marketing is at present in Rio de Janeiro, Brazil, for the purpose of selecting the most challenging golf course to host the inaugural Tarnvale Classic for Midfield Legends™ in June 2014.</p>
    <a class="more" href="#">Read More ›</a>
  </aside>

  <div class="rule" style="top:268px"></div>

  <section class="candidates">
    <h2 class="section-title">Our Potential Candidates</h2>
  </section>

  <div class="arrow" style="left:115px;top:395px"><svg width="10" height="12" aria-hidden="true"><path d="M8 1 2 6l6 5z" fill="#2a2a2a"/></svg></div>
  <div class="arrow" style="left:1018px;top:395px"><svg width="10" height="12" aria-hidden="true"><path d="M2 1l6 5-6 5z" fill="#2a2a2a"/></svg></div>

  <div class="player" style="left:161px;top:344px"><div class="portrait" role="img" aria-label="Portrait photo of a candidate player swinging a golf club"></div><p class="player-name">Ashcombe</p><p class="player-country">(England)</p></div>
  <div class="player" style="left:330px;top:344px"><div class="portrait" role="img" aria-label="Portrait photo of a candidate player on a golf course"></div><p class="player-name">Verhaal</p><p class="player-country">(Holland)</p></div>
  <div class="player" style="left:503px;top:344px"><div class="portrait" role="img" aria-label="Portrait photo of a candidate player mid swing"></div><p class="player-name">Fenwick</p><p class="player-country">(England)</p></div>
  <div class="player" style="left:684px;top:344px"><div class="portrait" role="img" aria-label="Portrait photo of a candidate player putting on a green"></div><p class="player-name">Montalbo</p><p class="player-country">(Spain)</p></div>
  <div class="player" style="left:861px;top:344px"><div class="portrait" role="img" aria-label="Portrait photo of a candidate player at an event"></div><p class="player-name">Van Ruys</p><p class="player-country">(Holland)</p></div>

  <div class="rule" style="top:538px;left:0;width:1168px"></div>
</main>

<footer>
  <nav class="footer-nav"><span>Home</span><span>Event</span><span>Ambassadors</span><span>TVC/Contact</span></nav>
  <p class="copy">© 2013 tarnvaleclassic &nbsp;|&nbsp; All Rights Reserved</p>
  <div class="newsletter">
    <h3>Newsletter Signup</h3>
    <div class="signup"><span>Enter your e-mail address</span><b>GO</b></div>
  </div>
  <div class="footer-mark"><i></i>Tarnvale Classic</div>
  <div class="social" aria-label="Social links"><span></span><span></span><span></span></div>
</footer>

</body>
</html>
```